Stainless Steel Water Bottle Packaging

We need a design for our cylindrical water bottle packaging.

Please see attached template (500ml cola bottle template .ai file) for exact dimensions.

VORO is defined as the elemental forces of nature embodied in an object or person. The design should be eye catching and draw potential clients in. Although its a cylindrical bottle/box, the front which would face the customer when sitting on a shelf should clearly display our logo.

Industry/Entity Type

Steel

Requirements
Must have
• Designed to the specifications of the attached template (see attached)
• Our VORO Logo (see attached) and website www.vorobottle.example(in smaller font) must appear.
• Size of bottle must appear - '17 oz/500 ml'
• These should appear somewhere:
• 'INULATED DOUBLE-WALL STAINLESS STEEL WATER BOTTLE'
• 'VORO Bottles magically keeps drinks cold for up to 24hrs, hot for 12',
• 'BPA Free'
• 'For every VORO bottle purchased, a portion of proceeds will go towards charity. Each of our colour's have been assigned a specific charity. Please visit www.vorobottle.example to find out which charity you helped support!'
• The Top circle - just our Symbol (flame/drop)
• The bottom circle - 'Inc. Designed in Canada made in China' on the outer edge leaving the middle empty for the UPC code.
• Reference website for the bottle case I'm looking for:
• http://shopkorinday.example/t-flow-lagoon-pink-insulated-water-bottle
Nice to have
• illustration of our water bottle shape (see attached) appearing somewhere on the box is something i had in mind but definitely not necessary.

```html
<!DOCTYPE html>
<html lang="en">
<head>
<meta charset="utf-8">
<title>VORO Bottle Packaging Dieline</title>
<link rel="stylesheet" href="https://fonts.googleapis.com/css2?family=Roboto:wght@400;500;700&family=Roboto+Condensed:wght@400;500;700&display=swap">
<style>
  :root {
    --paper: #f7f6fb;
    --white: #ffffff;
    --board: #2a2726;
    --board-soft: #35312f;
    --cut: #d9333f;
    --blue: #35a9dd;
    --yellow: #f7c21e;
    --green: #1f9a4b;
    --ink: #333333;
  }
  html, body {
    margin: 0;
    width: 1200px;
    height: 1200px;
    overflow: hidden;
    background: var(--paper);
  }
  .sheet {
    position: relative;
    width: 1033px;
    height: 1033px;
    transform: scale(1.16167);
    transform-origin: 0 0;
    font-family: "Roboto", Arial, sans-serif;
  }
  .lid-top, .lid-bottom {
    position: absolute;
    top: 29px;
    width: 206px;
    height: 206px;
    border-radius: 50%;
    border: 1px solid var(--cut);
    box-sizing: border-box;
  }
  .lid-top {
    left: 267px;
    background: var(--white);
    display: flex;
    align-items: center;
    justify-content: center;
    gap: 8px;
  }
  .lid-top .brand-dot {
    width: 14px; height: 14px; border-radius: 50%;
    background: var(--yellow);
  }
  .lid-top .brand-name {
    font-weight: 500;
    font-size: 40px;
    letter-spacing: 3px;
    color: var(--blue);
  }
  .lid-bottom {
    left: 489px;
    top: 23px;
    background: var(--board);
  }
  .lid-bottom svg { position: absolute; inset: 0; }
  .lid-bottom .edge-text {
    font-family: "Roboto Condensed", Arial, sans-serif;
    font-size: 15px;
    fill: var(--blue);
  }

  .wrap {
    position: absolute;
    left: 170px;
    top: 242px;
    width: 687px;
    height: 776px;
    background: var(--board);
    border: 1px solid var(--cut);
    box-sizing: border-box;
  }
  .wrap .top-panel {
    position: absolute;
    left: 0; top: 0;
    width: 100%;
    height: 171px;
    background: var(--white);
    border-bottom: 1px solid var(--cut);
    box-sizing: border-box;
  }
  .fold-line {
    position: absolute;
    background: var(--cut);
  }
  .fold-top { left: 25px; right: 0; top: 26px; height: 1px; }
  .fold-glue { left: 25px; top: 0; bottom: 0; width: 1px; }
  .fold-bottom { left: 25px; right: 0; bottom: 25px; height: 1px; }

  .brand-lockup {
    position: absolute;
    left: 25px; right: 0;
    top: 68px;
    text-align: center;
  }
  .brand-lockup .brand-row {
    display: flex;
    justify-content: center;
    align-items: center;
    gap: 12px;
  }
  .brand-lockup .brand-dot {
    width: 18px; height: 18px; border-radius: 50%;
    background: var(--yellow);
  }
  .brand-lockup .brand-name {
    font-weight: 500;
    font-size: 58px;
    line-height: 56px;
    letter-spacing: 6px;
    color: var(--blue);
  }
  .brand-lockup .site {
    margin-top: 2px;
    font-size: 16px;
    letter-spacing: 2.2px;
    color: var(--ink);
  }

  .claim-band {
    position: absolute;
    left: 70px;
    top: 171px;
    width: 42px;
    height: 579px;
    background: var(--yellow);
  }
  .vertical-text {
    position: absolute;
    white-space: nowrap;
    transform-origin: 0 0;
    transform: rotate(-90deg);
    font-family: "Roboto", Arial, sans-serif;
  }
  .claim-text {
    left: 80px;
    top: 746px;
    font-size: 20.5px;
    line-height: 22px;
    color: var(--board);
  }
  .promise-text {
    left: 116px;
    top: 744px;
    font-size: 18.5px;
    line-height: 22px;
    color: var(--blue);
  }

  .bottle-art {
    position: absolute;
    left: 262px;
    top: 196px;
    width: 140px;
    height: 509px;
  }
  .bottle-art .art-fill {
    position: absolute; inset: 0;
    border-radius: 44px 44px 22px 22px;
    background: linear-gradient(180deg, var(--board-soft), #3b3735);
    border: 2px solid rgba(255,255,255,0.85);
    box-sizing: border-box;
  }
  .bottle-art .badge {
    position: absolute;
    left: 26px; top: 137px;
    width: 78px; height: 78px;
    border-radius: 50%;
    border: 3px solid var(--green);
    box-sizing: border-box;
    display: flex;
    flex-direction: column;
    align-items: center;
    justify-content: center;
    font-family: "Roboto Condensed", Arial, sans-serif;
    font-weight: 700;
    color: var(--green);
    line-height: 1;
  }
  .bottle-art .badge .bpa { font-size: 24px; }
  .bottle-art .badge .free { font-size: 17px; margin-top: 1px; }
  .bottle-art .mini-brand {
    position: absolute;
    left: 0; right: 0;
    bottom: 26px;
    display: flex;
    justify-content: center;
    align-items: center;
    gap: 5px;
  }
  .bottle-art .mini-brand .brand-dot {
    width: 8px; height: 8px; border-radius: 50%;
    background: var(--yellow);
  }
  .bottle-art .mini-brand .brand-name {
    font-weight: 500;
    font-size: 22px;
    letter-spacing: 2px;
    color: var(--blue);
  }
  .volume {
    position: absolute;
    left: 232px; width: 200px;
    top: 716px;
    text-align: center;
    font-size: 16px;
    color: var(--blue);
  }

  .charity-note {
    position: absolute;
    left: 442px;
    top: 559px;
    width: 222px;
    font-size: 13.6px;
    line-height: 19.6px;
    color: var(--blue);
  }
  .charity-note p { margin: 0; }
  .charity-note .lead { color: var(--white); }
  .charity-note .brand-inline { color: var(--blue); font-weight: 500; letter-spacing: 1px; }
  .charity-note strong { color: var(--white); font-weight: 700; }
</style>
</head>
<body>
  <main class="sheet">
    <div class="lid-top" aria-label="Top lid">
      <span class="brand-dot"></span>
      <span class="brand-name">VORO</span>
    </div>

    <div class="lid-bottom" aria-label="Bottom lid">
      <svg width="206" height="206" viewBox="0 0 206 206">
        <defs>
          <path id="edge-arc" d="M 16,118 A 88 88 0 1 1 190,118"/>
        </defs>
        <text class="edge-text">
          <textPath href="#edge-arc" startOffset="50%" text-anchor="middle" textLength="272" lengthAdjust="spacing">INC. DESIGNED IN CANADA MADE IN CHINA</textPath>
        </text>
        <circle cx="33" cy="100" r="6" fill="none" stroke="var(--cut)" stroke-width="1"/>
        <circle cx="171" cy="99" r="6" fill="none" stroke="var(--cut)" stroke-width="1"/>
      </svg>
    </div>

    <section class="wrap">
      <div class="top-panel">
        <div class="brand-lockup">
          <div class="brand-row">
            <span class="brand-dot"></span>
            <span class="brand-name">VORO</span>
          </div>
          <div class="site">www.vorobottle.example</div>
        </div>
      </div>

      <span class="fold-line fold-top"></span>
      <span class="fold-line fold-glue"></span>
      <span class="fold-line fold-bottom"></span>

      <div class="claim-band"></div>
      <div class="vertical-text claim-text">INULATED DOUBLE-WALL STAINLESS STEEL WATER BOTTLE</div>
      <div class="vertical-text promise-text">VORO Bottles magically keeps drinks cold for up to 24hrs, hot for 12</div>

      <div class="bottle-art">
        <div class="art-fill" role="img" aria-label="Outline illustration of the VORO water bottle"></div>
        <div class="badge">
          <span class="bpa">BPA</span>
          <span class="free">FREE</span>
        </div>
        <div class="mini-brand">
          <span class="brand-dot"></span>
          <span class="brand-name">VORO</span>
        </div>
      </div>
      <div class="volume">17 oz/500 ml</div>

      <div class="charity-note">
        <p class="lead">For every <span class="brand-inline">VORO</span> bottle purchased, a portion of proceeds will go towards charity.</p>
        <p>Each of our colour's have been assigned a specific charity.</p>
        <p>Please visit <strong>www.vorobottle.example</strong> to find out which charity you helped support!</p>
      </div>
    </section>
  </main>
</body>
</html>
```